Web Pages Improvement, Update of existing MIRB website

Redesign existing website www.mirb.asn.au The # of pages can be reduced to a total of 6 including the home page. We have a design project out for the logo for this site so feel free to bid for that also.
As this is a simple brief with basic pages, we expect the end result to be code ready for uploaded to our existing host.

```html
<!DOCTYPE html>
<html lang="en">
<head>
<meta charset="utf-8">
<title>MIRB – Overview</title>
<link href="https://fonts.googleapis.com/css2?family=Open+Sans:wght@400;600;700&family=PT+Serif:wght@400;700&display=swap" rel="stylesheet">
<style>
:root{
  --bg-deep:#020a3a;
  --bg-glow:#1a4fd0;
  --orange:#f57a12;
  --page:#ffffff;
  --nav-top:#e3e9ef;
  --nav-bottom:#a9b6c3;
  --nav-line:#6f8497;
  --nav-text:#3b4c5c;
  --nav-active:#3a5f8a;
  --heading:#4a4a4a;
  --body-text:#9a9a9a;
  --blue-text:#2f5797;
  --footer-top:#c9d3dc;
  --footer-bottom:#a3b1bf;
  --footer-text:#2a2a2a;
}
*{margin:0;padding:0;box-sizing:border-box}
html,body{width:856px;height:1200px;overflow:hidden}
body{
  background:radial-gradient(ellipse at 30% 45%,var(--bg-glow) 0%,#0b2a9a 30%,var(--bg-deep) 75%);
  font-family:"PT Serif",Georgia,serif;
  position:relative;
}
.site-header{position:absolute;left:0;top:0;width:856px;height:123px;text-align:center}
.brand-name{position:absolute;left:0;width:856px;top:16px;font-family:"Open Sans",Arial,sans-serif;font-weight:700;font-size:70px;line-height:76px;color:var(--orange);letter-spacing:6px}
.brand-tagline{position:absolute;left:0;width:856px;top:98px;font-family:"Open Sans",Arial,sans-serif;font-weight:700;font-size:12px;color:#fff}
.page{position:absolute;left:87px;top:123px;width:684px;height:1010px;background:var(--page)}
.main-nav{display:flex;height:130px;background:linear-gradient(var(--nav-top),var(--nav-bottom));border-bottom:7px solid var(--nav-line)}
.nav-item{flex:1;border-right:1px solid #8d9dac;text-align:center;padding-top:24px;font-family:"Open Sans",Arial,sans-serif;font-weight:600;font-size:11.5px;letter-spacing:1px;color:var(--nav-text);line-height:13px;position:relative}
.nav-item:last-child{border-right:none}
.nav-item.is-active{color:var(--nav-active)}
.nav-item svg{position:absolute;left:50%;top:54px;margin-left:-17px}
.hero{position:absolute;left:13px;top:137px;width:658px;height:230px}
.hero-switch{position:absolute;left:0;top:37px;width:103px;height:159px;background:radial-gradient(circle at 50% 45%,#f7b45a,#d86a0c 70%,#b8560a);border:2px solid #f3a14a;box-shadow:2px 3px 6px rgba(0,0,0,.35)}
.hero-map{position:absolute;left:460px;top:0;width:198px;height:225px;background:radial-gradient(ellipse at 60% 50%,#e6e6e6,#f4f4f4 70%,#fff)}
.hero-title{position:absolute;left:130px;top:62px;font-size:22px;color:#1c1c1c}
.hero-title .name{color:var(--orange);font-weight:700;font-size:34px}
.hero-lead{position:absolute;left:155px;top:113px;font-size:14.5px;line-height:20px;color:var(--blue-text)}
.slider-bar{position:absolute;left:13px;top:368px;width:658px;height:26px;background:linear-gradient(#f4f4f4,#d8dbe0);border-radius:3px}
.slider-dots{position:absolute;right:8px;top:8px;display:flex;gap:4px}
.slider-dots span{width:11px;height:11px;border-radius:50%;background:#b5bcc6}
.slider-dots span.is-current{background:#3d6aa8}
.overview{position:absolute;left:13px;top:408px;width:658px}
.overview h1{font-family:"Open Sans",Arial,sans-serif;font-weight:600;font-size:21px;color:var(--orange);margin-bottom:14px}
.overview h2{font-weight:400;font-size:15.5px;color:var(--heading);margin-bottom:20px}
.overview p{font-size:10.2px;line-height:12.6px;color:var(--body-text);margin-bottom:12px}
.mark-row{display:flex;gap:20px;margin-top:14px}
.site-footer{position:absolute;left:0;top:760px;width:684px;height:250px;background:linear-gradient(var(--footer-top),var(--footer-bottom));color:var(--footer-text)}
.footer-col{position:absolute;top:20px}
.footer-col h3{font-size:12px;font-weight:700;margin-bottom:14px}
.footer-col h4{font-size:11px;font-weight:700;margin-bottom:10px}
.sitemap a{display:block;font-size:10px;line-height:11.4px;color:var(--footer-text);text-decoration:none}
.links-list a{display:block;font-size:7.6px;line-height:10px;margin-bottom:10px;color:var(--footer-text);text-decoration:none}
.copyright{position:absolute;right:17px;top:224px;font-family:"Open Sans",Arial,sans-serif;font-size:9px;font-weight:600}
</style>
</head>
<body>
<header class="site-header">
  <div class="brand-name">MIRB</div>
  <div class="brand-tagline">Measurement Instrument Review Board</div>
</header>

<div class="page">
  <nav class="main-nav">
    <div class="nav-item is-active">OVERVIEW<svg width="34" height="50"><rect x="10" y="0" width="14" height="5" fill="#ccc"/><rect x="2" y="5" width="30" height="40" rx="3" fill="#f2f2f2" stroke="#bbb"/><ellipse cx="17" cy="47" rx="15" ry="3" fill="#999" opacity=".3"/></svg></div>
    <div class="nav-item">STATEMENT OF<br>PURPOSE<svg width="34" height="50"><rect x="10" y="0" width="14" height="5" fill="#ccc"/><rect x="2" y="5" width="30" height="40" rx="3" fill="#f2f2f2" stroke="#bbb"/><rect x="3" y="36" width="28" height="8" fill="#e0282e"/></svg></div>
    <div class="nav-item">TYPE OF TESTING<svg width="34" height="50"><rect x="10" y="0" width="14" height="5" fill="#ccc"/><rect x="2" y="5" width="30" height="40" rx="3" fill="#f2f2f2" stroke="#bbb"/><rect x="3" y="30" width="28" height="7" fill="#5fd14a"/><rect x="3" y="37" width="28" height="7" fill="#e0282e"/></svg></div>
    <div class="nav-item">MEMBERS<svg width="34" height="50"><rect x="10" y="0" width="14" height="5" fill="#ccc"/><rect x="2" y="5" width="30" height="40" rx="3" fill="#f2f2f2" stroke="#bbb"/><rect x="3" y="16" width="28" height="28" fill="#3fcf3a"/></svg></div>
    <div class="nav-item">CONTACT<svg width="34" height="50"><rect x="10" y="0" width="14" height="5" fill="#ccc"/><rect x="2" y="5" width="30" height="40" rx="3" fill="#f5a93a" stroke="#c98a2a"/><path d="M19 12 L11 27 H17 L14 39 L23 22 H17 Z" fill="#333"/></svg></div>
    <div class="nav-item">LINKS<svg width="34" height="50"><rect x="10" y="0" width="14" height="5" fill="#ccc"/><rect x="2" y="5" width="30" height="40" rx="3" fill="#4fe04a" stroke="#36a832"/><path d="M12 18 V24 M22 18 V24 M9 24 H25 V29 Q17 36 9 29 Z M17 34 V40" stroke="#fff" stroke-width="2" fill="none"/></svg></div>
  </nav>

  <section class="hero">
    <div class="hero-switch" role="img" aria-label="Orange toggle switch photograph"></div>
    <div class="hero-map" role="img" aria-label="Faint map of Australia with state names"></div>
    <div class="hero-title"><span class="name">MIRB</span> was established in 1995</div>
    <div class="hero-lead">to foster the growth of a professional and<br>value adding compliance testing resource<br>to serve the needs of Australian industry.</div>
  </section>
  <div class="slider-bar"><div class="slider-dots"><span class="is-current"></span><span></span><span></span><span></span></div></div>

  <section class="overview">
    <h1>Overview</h1>
    <h2>Measurement Instrument Review Board</h2>
    <p>The Measurement Instrument Review Board of Australia (MIRB) was established in 1995 to foster the growth of a professional and value adding compliance testing resource to serve the needs of Australian industry.</p>
    <p>MIRB is an incorporated association formed by NTLA accredited electrical testing laboratories in Australia and includes an accredited member from New Zealand. The association has 14 active members which operate laboratories in a total of 18 locations in Australia and New Zealand. The members provide testing services to the public in the areas of electrical safety, electromagnetic compatibility, electromagnetic radiation, electromedical equipment, energy efficiency labelling, environmental performance, gas appliances, lighting equipment, performance ratings, and telecommunications. The NTLA accreditation mark is shown below.</p>
    <p>The Association operates a paid secretariat to service the interests of its members and to provide information about the services available to the public from its members. The registered office is in Brunswick, Victoria. The members of MIRB meet regularly to discuss issues of interest to its members and the testing industry and to make submissions to regulators, public investigations, inquiries and industry surveys. The Association nominates members to serve on relevant Committees of Norms Australia and to make representations to government inquiries.</p>
    <p>Member laboratories of MIRB test equipment to Australian and International Standards so that the clients are able to apply the appropriate regulatory mark for their product. The commonly recognised regulatory marks are the S-Mark and R-Mark for Australia, EU-Mark for Europe, NSB for the USA as shown below.</p>
    <div class="mark-row">
      <svg width="26" height="26"><rect x="2" y="2" width="22" height="22" fill="none" stroke="#222" stroke-width="2.5"/></svg>
      <svg width="26" height="26"><circle cx="13" cy="13" r="11" fill="#222"/></svg>
      <svg width="26" height="26"><rect x="3" y="3" width="20" height="20" fill="none" stroke="#222" stroke-width="2.5"/></svg>
      <svg width="26" height="26"><circle cx="13" cy="13" r="11" fill="none" stroke="#222" stroke-width="2.5"/></svg>
      <svg width="26" height="26"><rect x="2" y="2" width="22" height="22" fill="#222"/></svg>
    </div>
  </section>

  <footer class="site-footer">
    <div class="footer-col sitemap" style="left:15px">
      <h3>SITE MAP</h3>
      <a>Home</a><a>Overview</a><a>Statement of purpose</a><a>Types of testing</a><a>Member listing</a><a>New South Wales</a><a>Victoria</a><a>Queensland</a><a>South Australia</a><a>New Zealand</a><a>Members</a><a>Contact</a><a>Links</a>
    </div>
    <div class="footer-col links-list" style="left:190px;width:225px">
      <h3>LINKS</h3>
      <h4>Australia</h4>
      <a>National Testing Laboratories Authority, Australia</a>
      <a>Australian Signals and Media Office</a>
      <a>Norms Australia</a>
      <a>Australian Radiation and Nuclear Safety Office (ARNSO)</a>
      <a>Australian Product Safety Notices</a>
      <a>Electrical Regulators Forum</a>
    </div>
    <div class="footer-col links-list" style="left:428px;top:48px;width:240px">
      <h4>Overseas</h4>
      <a>Accreditation Services New Zealand</a>
      <a>Office of Enterprise - Radio Spectrum Unit (NZ)</a>
      <a>Norms New Zealand</a>
      <a>National Signals Bureau (USA)</a>
      <a>Continental Norms Committee</a>
    </div>
    <div class="copyright">Copyright © 2012 | MIRB</div>
  </footer>
</div>
</body>
</html>
```